Awesome photographers card for an awesome new business

Double sided business card Black background and silver logo in middle on one side. Details on otherside. please keep it simple

Photographer

Gavin Tolley
0482615073
GavinTolleyPhotography82@lumenpost.com
www.GavinTolleyPhotography.com.au
Instagram _Gavin_tolley

Requirements
Must have
• My logo in Silver
• please use instagram logo instead of "Instagram"

```html
<!DOCTYPE html>
<html lang="en">
<head>
<meta charset="utf-8">
<title>Gavin Tolley Photography – Business Card</title>
<link href="https://fonts.googleapis.com/css2?family=Bodoni+Moda:wght@500&family=Pathway+Gothic+One&display=swap" rel="stylesheet">
<style>
  :root {
    --backdrop-top: #0f63c6;
    --backdrop-bottom: #0d4a94;
    --card-dark-top: #5b5c5e;
    --card-dark-bottom: #0b0b0b;
    --card-light: #e6e6e6;
    --silver: #d9d9d9;
    --ink: #161616;
  }
  * { margin: 0; padding: 0; box-sizing: border-box; }
  html, body { width: 1200px; height: 1000px; overflow: hidden; }
  body {
    position: relative;
    background: linear-gradient(180deg, var(--backdrop-top), var(--backdrop-bottom));
    font-family: "Pathway Gothic One", "Arial Narrow", sans-serif;
  }
  .card { position: absolute; overflow: hidden; background: var(--card-light); }
  .card-front { left: 21px; top: 26px; width: 828px; height: 471px; }
  .card-back  { left: 347px; top: 514px; width: 820px; height: 467px; }
  .card-art { position: absolute; inset: 0; width: 100%; height: 100%; }

  .brand-mark {
    position: absolute;
    display: flex; align-items: center; gap: 16px;
    font-family: "Bodoni Moda", Georgia, serif;
    font-weight: 500;
    color: var(--silver);
    letter-spacing: 4px;
    white-space: nowrap;
  }
  .brand-mark .dot {
    width: 18px; height: 18px; border-radius: 50%;
    background: var(--silver); flex: none;
  }
  .card-front .brand-mark { left: 411px; top: 199px; transform: translate(-50%, -50%); font-size: 44px; }
  .card-back .brand-mark  { left: 201px; top: 226px; transform: translate(-50%, -50%); font-size: 36px; }

  .holder-name {
    position: absolute; left: 560px; top: 100px;
    font-family: "Pathway Gothic One", "Arial Narrow", sans-serif;
    font-weight: 400; font-size: 58px; line-height: 52px;
    letter-spacing: 3px; color: var(--ink);
  }
  .contact-list { position: absolute; left: 418px; top: 259px; list-style: none; }
  .contact-item {
    display: flex; align-items: center; gap: 16px;
    height: 54px; font-size: 24px; letter-spacing: 0; color: var(--ink);
    white-space: nowrap;
  }
  .contact-item svg { width: 28px; height: 28px; flex: none; }
</style>
</head>
<body>

<section class="card card-front" aria-label="Business card front">
  <svg class="card-art" viewBox="0 0 828 471" preserveAspectRatio="none" aria-hidden="true">
    <defs>
      <linearGradient id="dark-front" x1="0" y1="0" x2="0" y2="1">
        <stop offset="0" stop-color="#5b5c5e"/>
        <stop offset="1" stop-color="#0b0b0b"/>
      </linearGradient>
    </defs>
    <path d="M0,0 H828 V366 Q470,455 0,359 Z" fill="url(#dark-front)"/>
  </svg>
  <div class="brand-mark"><span class="dot"></span>GAVIN TOLLEY</div>
</section>

<section class="card card-back" aria-label="Business card back">
  <svg class="card-art" viewBox="0 0 820 467" preserveAspectRatio="none" aria-hidden="true">
    <defs>
      <linearGradient id="dark-back" x1="0" y1="0" x2="0" y2="1">
        <stop offset="0" stop-color="#5b5c5e"/>
        <stop offset="1" stop-color="#0b0b0b"/>
      </linearGradient>
    </defs>
    <path d="M0,0 H525 C480,40 445,110 440,190 C435,300 360,420 215,467 H0 Z" fill="url(#dark-back)"/>
  </svg>
  <div class="brand-mark"><span class="dot"></span>GAVIN TOLLEY</div>

  <h1 class="holder-name">GAVIN<br>TOLLEY</h1>

  <ul class="contact-list">
    <li class="contact-item">
      <svg viewBox="0 0 24 24" aria-hidden="true"><path fill="#161616" d="M6.6 10.8a15.1 15.1 0 0 0 6.6 6.6l2.2-2.2a1 1 0 0 1 1-.25 11.4 11.4 0 0 0 3.6.57 1 1 0 0 1 1 1V20a1 1 0 0 1-1 1A17 17 0 0 1 3 4a1 1 0 0 1 1-1h3.5a1 1 0 0 1 1 1c0 1.25.2 2.45.57 3.57a1 1 0 0 1-.25 1z"/></svg>
      0482615073
    </li>
    <li class="contact-item">
      <svg viewBox="0 0 24 24" aria-hidden="true"><rect x="2" y="5" width="20" height="14" fill="#161616"/><path d="M2 5l10 8 10-8" fill="none" stroke="#e6e6e6" stroke-width="1.5"/></svg>
      GavinTolleyPhotography82@lumenpost.com
    </li>
    <li class="contact-item">
      <svg viewBox="0 0 24 24" aria-hidden="true"><g fill="none" stroke="#161616" stroke-width="1.6"><circle cx="12" cy="12" r="9.5"/><ellipse cx="12" cy="12" rx="4" ry="9.5"/><path d="M2.5 12h19M4 7h16M4 17h16"/></g></svg>
      www.GavinTolleyPhotography.com.au
    </li>
    <li class="contact-item">
      <svg viewBox="0 0 24 24" aria-hidden="true"><circle cx="12" cy="12" r="9" fill="none" stroke="#161616" stroke-width="2"/></svg>
      _Gavin_tolley
    </li>
  </ul>
</section>

</body>
</html>
```